Vent doux

Hello,
I’m a designer sunglasses reatail Store owner in Montreal, Quebec.

Looking for something modern, fresh with a trendy appeal.

Will send my logo.
Thank you.

Store

```html
<!DOCTYPE html>
<html lang="fr">
<head>
<meta charset="utf-8">
<title>Vent doux — cartes de visite</title>
<link rel="stylesheet" href="https://fonts.googleapis.com/css2?family=Lato:wght@400;700&display=swap">
<style>
  :root {
    --stage: #ecebe8;
    --paper: #f7f7f6;
    --ink: #211f20;
    --brand-red: #d02a41;
    --brand-red-deep: #b51f36;
    --text-light: #f4f4f4;
    --text-muted: #c9c9c9;
  }
  * { box-sizing: border-box; margin: 0; padding: 0; }
  html, body { width: 1200px; height: 780px; overflow: hidden; }
  body {
    background: var(--stage);
    font-family: "Lato", Arial, sans-serif;
    position: relative;
  }
  .card {
    position: absolute;
    top: 240px;
    width: 520px;
    height: 300px;
    border-radius: 3px;
    overflow: hidden;
    box-shadow: 0 10px 24px rgba(0,0,0,0.18);
  }
  .card--front { left: 60px; background: var(--paper); }
  .card--back {
    left: 620px;
    background: radial-gradient(circle at 45% 40%, var(--brand-red) 0%, var(--brand-red-deep) 100%);
    display: flex;
    align-items: center;
    justify-content: center;
  }
  .card__shapes { position: absolute; inset: 0; width: 100%; height: 100%; }
  .brand-name {
    position: absolute;
    left: 22px;
    top: 52px;
    font-weight: 700;
    font-size: 34px;
    letter-spacing: 1px;
    color: var(--ink);
  }
  .contact {
    position: absolute;
    left: 22px;
    top: 140px;
    color: var(--text-light);
  }
  .contact__name { font-size: 19px; font-weight: 700; line-height: 1.1; }
  .contact__role { font-size: 13px; color: var(--brand-red); margin-bottom: 14px; }
  .contact__line { font-size: 13px; line-height: 1.45; }
  .contact__line--icon { display: flex; align-items: center; gap: 7px; }
  .contact__icon { width: 13px; height: 13px; flex: none; }
  .website {
    position: absolute;
    right: 18px;
    top: 244px;
    font-size: 13px;
    color: var(--text-light);
    letter-spacing: 0.3px;
  }
  .brand-name--back {
    font-weight: 700;
    font-size: 52px;
    letter-spacing: 2px;
    color: var(--text-light);
  }
</style>
</head>
<body>
  <section class="card card--front" aria-label="Recto de la carte">
    <svg class="card__shapes" viewBox="0 0 520 300" aria-hidden="true">
      <polygon points="0,0 232,0 272,300 0,300" fill="var(--ink)"/>
      <polygon points="0,38 237,38 247,118 0,118" fill="var(--paper)"/>
      <polygon points="292,238 520,238 520,272 300,272 286,255" fill="var(--brand-red)"/>
    </svg>
    <div class="brand-name">Vent doux</div>
    <div class="contact">
      <div class="contact__name">Léa Moreau</div>
      <div class="contact__role">Fondatrice</div>
      <div class="contact__line">PO BOX 418 rue Laurier</div>
      <div class="contact__line">Plateau, Montréal</div>
      <div class="contact__line contact__line--icon">
        <svg class="contact__icon" viewBox="0 0 14 14" aria-hidden="true"><circle cx="7" cy="7" r="7" fill="var(--brand-red)"/><rect x="4.5" y="3.5" width="5" height="7" rx="1" fill="none" stroke="#fff" stroke-width="1.1"/></svg>
        (514) 555-0142
      </div>
      <div class="contact__line contact__line--icon">
        <svg class="contact__icon" viewBox="0 0 14 14" aria-hidden="true"><circle cx="7" cy="7" r="7" fill="var(--brand-red)"/><rect x="3.5" y="4.5" width="7" height="5" fill="none" stroke="#fff" stroke-width="1.1"/><polyline points="3.5,4.5 7,7.5 10.5,4.5" fill="none" stroke="#fff" stroke-width="1.1"/></svg>
        bonjour@ventdoux.ca
      </div>
    </div>
    <div class="website">www.ventdoux.ca</div>
  </section>

  <section class="card card--back" aria-label="Verso de la carte">
    <div class="brand-name--back">Vent doux</div>
  </section>
</body>
</html>
```